Mesa Brew Circle - A Monthly Subscription Coffee Club - Shopify Website Design

A monthly subscription company. Need a Shopify Website Design and uploaded to fully work with Tidal Recurrings.

Please look at these sites for examples as well as the images I enclosed.

https://www.sipvantor.example/
https://grindcrate.example/
https://www.plattermint.example/
https://www.globalnibblory.example/

Number of Pages Required

1 page

```html
<!DOCTYPE html>
<html lang="en">
<head>
<meta charset="utf-8">
<title>Mesa Brew Circle — Monthly Subscription Coffee Club</title>
<link href="https://fonts.googleapis.com/css2?family=Playfair+Display:wght@700;900&family=Montserrat:wght@400;500;600;700&display=swap" rel="stylesheet">
<style>
:root{
  --brown:#5b2f1f;
  --brown-dark:#3b1f14;
  --ink:#1f1b19;
  --text:#555;
  --white:#fff;
  --light:#f3f2f0;
  --footer:#2a2624;
  --footer-text:#bdb6b0;
  --serif:'Playfair Display', Georgia, serif;
  --sans:'Montserrat', Arial, sans-serif;
}
*{box-sizing:border-box;margin:0;padding:0}
html,body{width:1200px;height:5008px;overflow:hidden}
body{font-family:var(--sans);color:var(--ink);background:var(--white);position:relative}
section,header,footer{position:relative;width:1200px;overflow:hidden}
.photo{position:absolute}
.btn{display:inline-block;font-family:var(--sans);font-weight:600;font-size:15px;letter-spacing:1px;text-transform:uppercase;padding:14px 26px;text-decoration:none}
.btn-outline{border:2px solid var(--white);color:var(--white)}
.btn-solid{background:var(--brown);color:var(--white)}
.rule{width:80px;height:4px;background:var(--brown)}
.para{font-size:15px;line-height:1.75;color:var(--text)}

/* hero */
.hero{height:600px;background:linear-gradient(100deg,#1c130d 0%,#3a2618 45%,#5a3c26 75%,#2a1b11 100%)}
.hero .photo{right:130px;top:150px;width:450px;height:440px;border-radius:6px;background:radial-gradient(circle at 55% 45%,#e9e4de 0%,#b59878 35%,#6b4226 65%,transparent 80%)}
.nav{position:absolute;top:0;left:0;width:1200px;height:90px;display:flex;align-items:center;justify-content:space-between;padding:0 170px}
.brand{font-family:var(--serif);font-weight:700;font-size:24px;color:var(--white);letter-spacing:1px;text-transform:uppercase}
.hero-copy{position:absolute;left:176px;top:170px;color:var(--white)}
.hero-copy h1{font-family:var(--serif);font-weight:900;font-size:50px;line-height:1.15;text-transform:uppercase;letter-spacing:2px}
.hero-copy h2{font-family:var(--serif);font-weight:700;font-size:38px;text-transform:uppercase;margin-top:10px;letter-spacing:1px}
.hero-copy .btn{margin-top:40px}

/* about */
.about{height:480px}
.about .photo{left:160px;top:110px;width:440px;height:240px;background:radial-gradient(ellipse at 50% 60%,#6b3c1e 0%,#3e2010 45%,#fff 72%)}
.about-copy{position:absolute;left:646px;top:118px;width:400px}
.about-copy h3{font-family:var(--serif);font-weight:900;font-size:30px;color:var(--brown);text-transform:uppercase;margin:22px 0 20px}
.about-copy .btn{margin-top:20px}

/* video */
.video{height:560px;background:linear-gradient(90deg,#1a1410 0%,#3b2b20 40%,#7a5b3e 70%,#c59a52 100%)}
.video .photo{inset:0}
.play{position:absolute;left:560px;top:240px}

/* plans */
.plans-intro{height:272px;text-align:center}
.plans-intro .rule{margin:100px auto 0}
.plans-intro h3{font-family:var(--serif);font-weight:900;font-size:32px;text-transform:uppercase;margin-top:22px}
.plans-intro .para{width:860px;margin:14px auto 0;font-size:14px}
.tiles{height:368px;display:flex}
.tile{flex:1;position:relative;display:flex;align-items:center;justify-content:center}
.tile:nth-child(1){background:linear-gradient(135deg,#2b1d14,#6a4a33)}
.tile:nth-child(2){background:linear-gradient(135deg,#5d4c40,#b4a290)}
.tile:nth-child(3){background:linear-gradient(135deg,#4a2a1a,#a5714a)}
.tile span{color:var(--white);font-weight:600;font-size:20px;letter-spacing:1px;text-transform:uppercase}

/* club */
.club{height:472px;background:linear-gradient(90deg,#f4f3f2 0%,#ebeae8 60%,#d9d4cd 100%)}
.club .photo{right:0;top:40px;width:430px;height:432px;background:radial-gradient(ellipse at 60% 60%,#c9a57f 0%,#e1d2c0 45%,transparent 75%)}
.club-copy{position:absolute;left:176px;top:100px;width:450px}
.club-copy h3{font-family:var(--serif);font-weight:900;font-size:30px;text-transform:uppercase;margin:20px 0 16px;color:var(--ink)}
.club-copy .btn{margin-top:24px}

/* split products */
.split{height:868px;display:flex}
.split .photo{position:relative;width:600px;height:868px;background:linear-gradient(160deg,#0d0b0a 0%,#3a2a20 40%,#7b5d44 70%,#c8b7a4 100%)}
.product-list{width:600px;background:var(--light);display:flex;flex-direction:column;align-items:center;padding-top:72px}
.product{display:flex;flex-direction:column;align-items:center;height:272px}
.product .thumb{width:140px;height:120px;border-radius:4px}
.product:nth-child(1) .thumb{background:linear-gradient(180deg,#e3d4bf,#b08d63)}
.product:nth-child(2) .thumb{background:linear-gradient(180deg,#e6d3b5,#c39a69)}
.product:nth-child(3) .thumb{background:linear-gradient(180deg,#c9b8a5,#3a2418)}
.product h4{font-size:15px;font-weight:600;text-transform:uppercase;letter-spacing:1px;margin:24px 0 14px}
.product .btn{font-size:11px;padding:9px 16px}

/* coffee box */
.shop{height:580px}
.shop .photo{left:176px;top:80px;width:432px;height:408px;background:linear-gradient(135deg,#eceae7,#d6d2cd)}
.shop-panel{position:absolute;left:696px;top:130px;width:330px;text-align:center}
.shop-panel h3{font-family:var(--serif);font-weight:900;font-size:30px;color:var(--brown);text-transform:uppercase}
.price{font-size:16px;color:var(--text);margin-top:12px}
.qty{margin-top:20px;height:46px;background:#eeeded;border:1px solid #ddd;display:flex;align-items:center;justify-content:space-between;padding:0 14px;font-size:13px;color:#444}
.cart{margin-top:14px;height:46px;border:1px solid #bbb;display:flex;align-items:center;justify-content:center;font-size:13px;letter-spacing:1px;text-transform:uppercase}
.buy{margin-top:12px;height:46px;background:var(--brown);color:var(--white);display:flex;align-items:center;justify-content:center;font-size:13px;letter-spacing:1px;text-transform:uppercase}
.details{margin-top:22px;font-size:13px;letter-spacing:1px;text-transform:uppercase;display:flex;align-items:center;justify-content:center;gap:10px}

/* cta */
.cta{height:508px;background:linear-gradient(180deg,#1e1712 0%,#33261d 50%,#4d3a2b 100%);text-align:center;color:var(--white)}
.cta .photo{inset:0;background:radial-gradient(ellipse at 70% 80%,rgba(150,110,70,.45),transparent 60%)}
.cta-copy{position:relative;padding-top:130px}
.cta-copy h3{font-family:var(--serif);font-weight:900;font-size:40px;text-transform:uppercase;letter-spacing:1px}
.cta-copy h4{font-family:var(--serif);font-weight:700;font-size:30px;text-transform:uppercase;margin-top:4px}
.cta-copy p{font-size:16px;margin-top:20px;color:#e8e2dc}
.cta-copy .btn{margin-top:40px}

/* footer */
.site-footer{height:300px;background:var(--footer);color:var(--footer-text);font-size:14px}
.foot-links{position:absolute;left:170px;top:50px;list-style:none;line-height:44px;text-transform:uppercase;letter-spacing:1px}
.signup{position:absolute;left:476px;top:50px;width:380px}
.signup h5{font-family:var(--serif);font-weight:700;font-size:18px;color:var(--white);text-transform:uppercase}
.signup p{margin-top:10px;font-size:13px}
.signup .field{margin-top:40px;border-bottom:1px solid #777;display:flex;justify-content:space-between;padding-bottom:10px;font-size:12px}
.signup .field b{color:var(--white);font-weight:600;letter-spacing:1px}
.copyright{position:absolute;left:170px;top:258px;font-size:12px}
.payments{position:absolute;left:822px;top:250px;display:flex;gap:6px}
.payments i{display:block;width:34px;height:22px;background:#e6e2de;border-radius:3px}
.currency{position:absolute;right:170px;top:254px;font-size:12px}
</style>
</head>
<body>

<header class="hero">
  <div class="photo" role="img" aria-label="Coffee mug with a heart of beans and a gift box on a dark wooden table"></div>
  <nav class="nav">
    <svg width="36" height="22" viewBox="0 0 36 22" aria-label="Menu"><g stroke="#fff" stroke-width="3"><line x1="0" y1="2" x2="36" y2="2"/><line x1="0" y1="11" x2="36" y2="11"/><line x1="0" y1="20" x2="36" y2="20"/></g></svg>
    <span class="brand">Mesa Brew Circle</span>
    <svg width="26" height="30" viewBox="0 0 26 30" aria-label="Cart"><g fill="none" stroke="#fff" stroke-width="2.5"><rect x="2" y="9" width="22" height="19"/><path d="M8 12V6a5 5 0 0 1 10 0v6"/></g></svg>
  </nav>
  <div class="hero-copy">
    <h1>Monthly<br>Subscription</h1>
    <h2>Coffee Club</h2>
    <a class="btn btn-outline" href="#">Shop Now</a>
  </div>
</header>

<section class="about">
  <div class="photo" role="img" aria-label="Pile of roasted coffee beans with a small shopping-cart box"></div>
  <div class="about-copy">
    <div class="rule"></div>
    <h3>About Mesa Brew Circle</h3>
    <p class="para">Nam libero tempore, cum soluta nobis est eligendi optio cumque nihil impedit quo minus id quod maxime placeat facere possimus, omnis dolor repellendus. Temporibus autem quibusdam et aut officiis debitis aut rerum necessitatibus saepe eveniet.</p>
    <a class="btn btn-solid" href="#">Shop Now</a>
  </div>
</section>

<section class="video">
  <div class="photo" role="img" aria-label="Hands holding a wrapped coffee gift box at a café table"></div>
  <svg class="play" width="80" height="80" viewBox="0 0 80 80" aria-label="Play video"><circle cx="40" cy="40" r="37" fill="none" stroke="#fff" stroke-width="4"/><path d="M32 25 L56 40 L32 55 Z" fill="none" stroke="#fff" stroke-width="4" stroke-linejoin="round"/></svg>
</section>

<section class="plans-intro">
  <div class="rule"></div>
  <h3>Monthly Subscription</h3>
  <p class="para">Nam libero tempore, cum soluta nobis est eligendi optio cumque nihil impedit quo minus id quod maxime placeat facere possimus, omnis dolor repellendus, omnis dolor repellendus.</p>
</section>

<section class="tiles">
  <div class="tile" role="img" aria-label="Coffee being served at a café counter"><span>Nam Libero Tempore</span></div>
  <div class="tile" role="img" aria-label="Person holding an open coffee delivery box"><span>Cum Soluta Nobis</span></div>
  <div class="tile" role="img" aria-label="Stacked kraft delivery boxes"><span>Impedit Quo Minus</span></div>
</section>

<section class="club">
  <div class="photo" role="img" aria-label="Paper coffee cups in a carrier beside a kraft bag"></div>
  <div class="club-copy">
    <div class="rule"></div>
    <h3>Mesa Brew Coffee Club</h3>
    <p class="para">Nam libero tempore, cum soluta nobis est eligendi optio cumque nihil impedit quo minus id quod maxime placeat facere possimus, omnis dolor repellendus. Temporibus autem quibusdam et aut officiis debitis aut rerum necessitatibus saepe eveniet.</p>
    <a class="btn btn-solid" href="#">Shop Now</a>
  </div>
</section>

<section class="split">
  <div class="photo" role="img" aria-label="Glass jar of instant coffee next to a cup of coffee"></div>
  <div class="product-list">
    <div class="product"><div class="thumb" role="img" aria-label="Coffee packaging set"></div><h4>Nam Libero Tempore</h4><a class="btn btn-solid" href="#">Shop Now</a></div>
    <div class="product"><div class="thumb" role="img" aria-label="Two kraft coffee bags"></div><h4>Nam Libero Tempore</h4><a class="btn btn-solid" href="#">Shop Now</a></div>
    <div class="product"><div class="thumb" role="img" aria-label="Two jars of ground coffee"></div><h4>Nam Libero Tempore</h4><a class="btn btn-solid" href="#">Shop Now</a></div>
  </div>
</section>

<section class="shop">
  <div class="photo" role="img" aria-label="Kraft coffee pouch next to a grey mug"></div>
  <div class="shop-panel">
    <h3>Coffee Box</h3>
    <p class="price">$600.00</p>
    <div class="qty"><span>Quantity</span><svg width="10" height="6" viewBox="0 0 10 6"><path d="M0 0 L5 6 L10 0Z" fill="#444"/></svg></div>
    <div class="cart">Add to Cart</div>
    <div class="buy">Buy It Now</div>
    <div class="details"><svg width="16" height="12" viewBox="0 0 16 12"><g stroke="#333" stroke-width="2"><line x1="0" y1="1" x2="16" y2="1"/><line x1="0" y1="6" x2="16" y2="6"/><line x1="0" y1="11" x2="16" y2="11"/></g></svg>Full Details</div>
  </div>
</section>

<section class="cta">
  <div class="photo" role="img" aria-label="Person packing coffee into a delivery box"></div>
  <div class="cta-copy">
    <h3>Monthly Subscription</h3>
    <h4>Coffee Club</h4>
    <p>Nam libero tempore, cum soluta nobis est eligendi optio cumque nihil impedit.</p>
    <a class="btn btn-outline" href="#">Shop Now</a>
  </div>
</section>

<footer class="site-footer">
  <ul class="foot-links"><li>Search</li><li>Articles</li><li>FAQs</li><li>Contact Us</li></ul>
  <div class="signup">
    <h5>Sign Up for Updates</h5>
    <p>Promotions, new products and sales. Directly to your inbox.</p>
    <div class="field"><span>Your email address</span><b>Subscribe →</b></div>
  </div>
  <p class="copyright">Copyright © 2020, Mesa Brew Circle. All Rights Reserved.</p>
  <div class="payments"><i></i><i></i><i></i><i></i><i></i><i></i><i></i></div>
  <span class="currency">CDS</span>
</footer>

</body>
</html>
```